Need Power Point Presentation - That incorporates New Logo

We have a new logo and would like to incorporate it into a Power Point template. We are looking for title page, 2 body pages and a closing page design. If you have any questions please let me know. New logo is attached.

```html
<!DOCTYPE html>
<html lang="en">
<head>
<meta charset="utf-8">
<title>Veltran – Title Slide</title>
<link rel="stylesheet" href="https://fonts.googleapis.com/css2?family=Cinzel:wght@500&display=swap">
<style>
  :root {
    --sky-deep: #0b3f7e;
    --sky-mid: #1a6db8;
    --sky-light: #5bb4e8;
    --teal: #138bb0;
    --teal-soft: #7cc6dc;
    --paper: #ffffff;
    --rule-grey: #cfd4d9;
    --brand-blue: #1a82c8;
  }
  html, body {
    margin: 0;
    padding: 0;
    width: 1200px;
    height: 658px;
    overflow: hidden;
    background: var(--paper);
  }
  .slide {
    position: relative;
    width: 1200px;
    height: 658px;
    overflow: hidden;
  }
  .slide-art {
    position: absolute;
    inset: 0;
    display: block;
  }
  .brand-name {
    position: absolute;
    left: 990px;
    top: 558px;
    margin: 0;
    font-family: "Cinzel", serif;
    font-weight: 500;
    font-size: 28px;
    letter-spacing: 1px;
    color: var(--brand-blue);
  }
</style>
</head>
<body>
<main class="slide">
  <svg class="slide-art" viewBox="0 0 1200 658" width="1200" height="658" xmlns="http://www.w3.org/2000/svg">
    <defs>
      <linearGradient id="sky" x1="0" y1="0" x2="1" y2="0.3">
        <stop offset="0" stop-color="var(--sky-deep)"/>
        <stop offset="0.55" stop-color="var(--sky-mid)"/>
        <stop offset="1" stop-color="var(--sky-light)"/>
      </linearGradient>
      <linearGradient id="floor" x1="0" y1="0" x2="1" y2="0">
        <stop offset="0" stop-color="var(--teal)"/>
        <stop offset="0.5" stop-color="var(--teal-soft)"/>
        <stop offset="0.85" stop-color="var(--paper)"/>
      </linearGradient>
      <clipPath id="band">
        <path d="M0,392 C250,440 500,432 700,380 C880,332 1020,220 1120,0 H1200 V392 C1000,510 800,575 560,575 C350,575 150,530 0,470 Z"/>
      </clipPath>
    </defs>

    <rect class="floor" width="1200" height="658" fill="url(#floor)"/>

    <g class="photo-strip" clip-path="url(#band)">
      <rect x="0" y="0" width="192" height="658" fill="#8a8f8c" role="img" aria-label="Industrial plant with smoking chimneys"/>
      <rect x="192" y="0" width="146" height="658" fill="#7a7560" role="img" aria-label="Worker in winter camouflage gear in the snow"/>
      <rect x="338" y="0" width="260" height="658" fill="#4f8fd6" role="img" aria-label="Blue leather aircraft cabin seats"/>
      <polygon points="598,0 700,0 760,658 598,658" fill="#9a8a72" role="img" aria-label="Crane lifting lumber at a port"/>
      <polygon points="700,0 850,0 850,658 760,658" fill="#355f5a" role="img" aria-label="Green and yellow locomotive"/>
      <polygon points="850,0 1000,0 1100,658 850,658" fill="#e7e4df" role="img" aria-label="Branded insulated bags and fabric panels"/>
      <polygon points="1000,0 1200,0 1200,658 1100,658" fill="#6c7f96" role="img" aria-label="Space station orbiting Earth"/>
    </g>

    <path class="band-edge-bottom" d="M1200,392 C1000,510 800,575 560,575 C350,575 150,530 0,470" fill="none" stroke="var(--rule-grey)" stroke-width="8"/>

    <path class="sky" d="M0,0 H1140 C1040,200 880,320 700,368 C500,420 250,426 0,372 Z" fill="url(#sky)"/>
    <path class="band-edge-top" d="M1140,0 C1040,200 880,320 700,368 C500,420 250,426 0,372" fill="none" stroke="var(--rule-grey)" stroke-width="14"/>
    <path class="band-edge-top-gap" d="M1152,0 C1050,212 890,332 702,382 C500,432 250,438 0,386" fill="none" stroke="var(--paper)" stroke-width="8"/>
  </svg>

  <p class="brand-name">VELTRAN®</p>
</main>
</body>
</html>
```